Global Educational start-up needs elegant website

Hi,
I am looking for a website for a company which is serving the high-end, demanding clients in China, on educational market and working internationally. The company name is Amber Harbor Educational Services. Please find attached its logo.
We need a website consisting of seven sites:
1. What do we do? (main/basic site)
2. Programs (two subsites under this site)
a) Leadership, Entrepreneurship and Personal Development (Europe)
b) Career incubator (UK)
3. Our mission and values
4. Who are we?
5. Testimonials
6. Contact us
7. Sign for a program! (button redirecting to a form)
We would appreciate simplicity, elegance and minimalizm. It should be interactive and should meet highest expectations of the rich cusomers. On the visual materials the Chinese children aged 13-20 are preferred, in link with education, development and so on.
Time is short so we might finish the contest in a moment we find a proper choice.
Target Market(s)
Parents of rich Chinese children.
Industry/Entity Type
Education

```html
<!DOCTYPE html>
<html lang="en">
<head>
<meta charset="utf-8">
<title>Amber Harbor Educational Services</title>
<link rel="stylesheet" href="https://fonts.googleapis.com/css2?family=Roboto:wght@300;400;500;700&display=swap">
<style>
  :root {
    --green: #45a845;
    --ink: #444444;
    --muted: #777777;
    --band-light: #ececec;
    --band-dark: #555555;
    --white: #ffffff;
    --black-btn: #2b2b2b;
  }
  * { margin: 0; padding: 0; box-sizing: border-box; }
  html, body { width: 1200px; height: 1198px; overflow: hidden; }
  body {
    position: relative;
    font-family: "Roboto", Arial, sans-serif;
    color: var(--ink);
    background: var(--white);
  }
  .abs { position: absolute; }

  .top-band {
    position: absolute; left: 0; top: 0; width: 1200px; height: 509px;
    background-color: var(--band-light);
    background-image: repeating-linear-gradient(45deg, rgba(255,255,255,.35) 0 2px, transparent 2px 4px);
    border-top: 3px solid var(--green);
  }
  .main-nav {
    position: absolute; top: 3px; left: 0; width: 1200px; height: 28px;
    background: #f6f6f6; border-bottom: 1px solid #e3e3e3;
    display: flex; justify-content: center; gap: 39px;
    font-size: 9px; line-height: 28px; color: #666;
  }
  .main-nav .active { color: var(--green); }

  .brand { left: 0; top: 58px; width: 1200px; text-align: center;
    font-size: 24px; font-weight: 300; color: #6f6f6f; line-height: 30px; }

  .hero { left: 270px; top: 116px; width: 650px; height: 273px;
    background: linear-gradient(100deg, #c9a77a 0%, #8a7060 35%, #d9d4cc 60%, #e9e6e2 100%); }
  .hero-caption { left: 473px; top: 321px; width: 243px; height: 18px; background: var(--green);
    color: #fff; font-size: 9.5px; font-weight: 700; text-align: center; line-height: 18px; }
  .hero-dots { left: 579px; top: 360px; display: flex; gap: 3px; }
  .hero-dots span { width: 10px; height: 10px; border-radius: 50%; background: #444; }
  .hero-dots span:first-child { background: var(--green); }

  .intro-col { top: 411px; width: 310px; }
  .intro-col h2 { font-size: 15px; font-weight: 300; color: #444; margin-bottom: 12px; }
  .intro-col p { font-size: 7.5px; line-height: 11px; color: #777; }
  .read-more { display: inline-block; margin-top: 11px; font-size: 6.5px; color: #777; text-decoration: underline; }

  .section-title { left: 0; width: 1200px; text-align: center; font-weight: 300; font-size: 19px; color: #555; }
  .section-lead { left: 410px; width: 380px; text-align: center; font-size: 7.5px; line-height: 11px; color: #666; }

  .feature-img { left: 270px; top: 629px; width: 222px; height: 132px; border: 1px solid #ddd;
    background: linear-gradient(120deg, #f4f4f4 0%, #c89a7c 30%, #5a6a8a 55%, #e8e8ea 100%); }
  .board { left: 527px; top: 627px; width: 220px; }
  .board h3, .support h3 { font-size: 10px; font-weight: 700; color: #444; margin-bottom: 12px; }
  .board p { font-size: 7.5px; line-height: 12px; color: #777; margin-bottom: 11px; }
  .support { left: 792px; top: 627px; }
  .support ul { list-style: none; }
  .support li { font-size: 8.5px; line-height: 17.6px; color: var(--green); text-decoration: underline; }

  .quote-band { left: 0; top: 797px; width: 1200px; height: 155px; background: var(--band-dark);
    background-image: repeating-linear-gradient(45deg, rgba(0,0,0,.06) 0 2px, transparent 2px 4px); }
  .quote-mark { left: 0; top: 824px; width: 1200px; text-align: center; color: #fff;
    font-family: Georgia, serif; font-size: 40px; font-weight: 700; line-height: 1; }
  .quote-text { left: 405px; top: 866px; width: 390px; text-align: center; color: #fff; font-size: 8.5px; line-height: 14px; }
  .quote-author { left: 0; top: 904px; width: 1200px; text-align: center; color: var(--green); font-size: 8.5px; }
  .arrow { top: 877px; }

  .signup-band { left: 0; top: 952px; width: 1200px; height: 75px; background: var(--green); }
  .signup-title { left: 299px; top: 977px; color: #fff; font-size: 19px; font-weight: 500; }
  .signup-input { left: 496px; top: 973px; width: 295px; height: 30px; background: #fff;
    color: var(--green); font-size: 10px; line-height: 30px; padding-left: 11px; }
  .signup-btn { left: 802px; top: 973px; width: 84px; height: 30px; background: var(--black-btn);
    color: #fff; font-size: 11px; font-weight: 500; text-align: center; line-height: 30px; }

  .contact-line { left: 0; top: 1096px; width: 1200px; text-align: center; font-size: 7px; color: #777; }
  .social { left: 549px; top: 1123px; display: flex; gap: 11px; }
  .social span { width: 20px; height: 20px; border-radius: 50%; background: #a8a8a8; }
  .footer-rule { left: 270px; top: 1162px; width: 650px; height: 1px; background: #cfcfcf; }
  .footer-note { left: 0; top: 1177px; width: 1200px; text-align: center; font-size: 7px; color: #666; }
</style>
</head>
<body>
  <div class="top-band"></div>
  <nav class="main-nav">
    <span class="active">Home</span><span>About Us</span><span>Departments</span><span>Schools</span><span>Blogs</span><span>Contact Us</span>
  </nav>

  <div class="abs brand">Amber Harbor Educational Services</div>

  <div class="abs hero" role="img" aria-label="Teacher helping a young student write in a bright classroom"></div>
  <div class="abs hero-caption">PREPARING STUDENTS FOR SUCCESSFUL FUTURE</div>
  <div class="abs hero-dots"><span></span><span></span><span></span></div>

  <div class="abs intro-col" style="left:270px">
    <h2>WELCOME!</h2>
    <p>Ruelloribus eget elementum vel curleif end elit. Aean auctoetnilir pis terios. ante ipsummis faulet utrice posere cubitsed leo pharetu nec augue. dui bibendum ornare elementum. In vel mi pellentesque.</p>
    <span class="read-more">READ MORE</span>
  </div>
  <div class="abs intro-col" style="left:604px">
    <h2>OUR MISSION &amp; VALUES</h2>
    <p>Ruelloribus eget elementum vel curleif end elit. Aean auctoetnilir pis terios. ante ipsummis faulet utrice posere cubitsed leo pharetu nec augue. dui bibendum ornare elementum. In vel mi pellentesque.</p>
    <span class="read-more">READ MORE</span>
  </div>

  <h2 class="abs section-title" style="top:536px">What do we do?</h2>
  <p class="abs section-lead" style="top:575px">Ut telloribus eget elemetum vel curleif end elit. Aean auctoetnilir pis. Nulla fn nec ero ante ipsummis faulet utrice posere cubitsed leo pharetu nec augue Ut placerat</p>

  <div class="abs feature-img" role="img" aria-label="Young students working at a desk with a laptop"></div>
  <div class="abs board">
    <h3>Board of Education</h3>
    <p>Lorem ipsum dolor sit amet consectetur adipiscing elit. Dnec dapius vulputate let eget hendrerit. Lorem ipsum dolor sit amet consectetur adipiscing elit.</p>
    <p>Dnec dapius vulputate let eget hendrerit. Lorem ipsum dolor sit amet consectetur adipiscing elit.</p>
    <span class="read-more" style="margin-top:2px">READ MORE</span>
  </div>
  <div class="abs support">
    <h3>Get Support</h3>
    <ul>
      <li>Grade 5-12</li><li>Acdmic Program</li><li>Continuing Education</li><li>Summer School</li><li>Student Handbook</li><li>Provincial Exam Practice</li>
    </ul>
  </div>

  <div class="abs quote-band"></div>
  <div class="abs quote-mark">&ldquo;</div>
  <p class="abs quote-text">Lorem ipsum dolor sit amet, consectetur adipiscing elit. Maurissemper eu turpis sed, mollis vehicula neque. Ut in urna ante. Etiam sit amet arcu ante.</p>
  <div class="abs quote-author">-Lorem Ipsum</div>
  <svg class="abs arrow" style="left:269px" width="10" height="14" viewBox="0 0 10 14" aria-hidden="true"><path d="M8 1 2 7l6 6" fill="none" stroke="#fff" stroke-width="2"/></svg>
  <svg class="abs arrow" style="left:911px" width="10" height="14" viewBox="0 0 10 14" aria-hidden="true"><path d="M2 1l6 6-6 6" fill="none" stroke="#fff" stroke-width="2"/></svg>

  <div class="abs signup-band"></div>
  <div class="abs signup-title">Sign for a program!</div>
  <div class="abs signup-input">Your Email Address</div>
  <div class="abs signup-btn">SUBMIT</div>

  <h2 class="abs section-title" style="top:1056px">Get in Touch</h2>
  <p class="abs contact-line">214 LANTERN QUAY, NORTHBAY, LQ 12 7AB TELEPHONE: +1 800 555 01234 &nbsp;FAX: +1 800 555 0199</p>
  <div class="abs social" aria-label="Social links"><span></span><span></span><span></span></div>
  <div class="abs footer-rule"></div>
  <p class="abs footer-note">Amber Harbor Educational Services &copy; 2014 | Privacy Policy</p>
</body>
</html>
```